Media buzzing film 'Harbor of Glass' needs a poster

Poster size is One Sheet 27" x 40" Also it should still be clear and captivating when shrunk to a thumbnail size like FLKV movie posters.

Target Market(s)

Specifically women age 20-55
Men 30-60

Industry/Entity Type

Movie

Requirements
Must have
• Harbor of Glass
Nice to have
• Harbor of Glass
Should not have
• Harbor of Glass

```html
<!DOCTYPE html>
<html lang="en">
<head>
<meta charset="utf-8">
<title>Harbor of Glass — One Sheet</title>
<link rel="stylesheet" href="https://fonts.googleapis.com/css2?family=Marcellus&family=Cormorant+Garamond:ital,wght@0,500;1,500&family=Questrial&display=swap">
<style>
  :root {
    --gold-top: #f9c21f;
    --gold-mid: #f6b11a;
    --gold-low: #f3a716;
    --veil-blue: #5bb8e6;
    --skin-orange: #ee8a3c;
    --ink: #1f1a16;
    --tagline: #f7e41c;
  }
  * { margin: 0; padding: 0; box-sizing: border-box; }
  html, body { width: 810px; height: 1200px; overflow: hidden; }
  body { background: var(--gold-mid); }

  .poster {
    position: relative;
    width: 810px;
    height: 1200px;
    overflow: hidden;
    background: linear-gradient(180deg, var(--gold-top) 0%, var(--gold-mid) 55%, var(--gold-low) 100%);
  }

  .key-art {
    position: absolute;
    left: 0; top: 0;
    width: 810px; height: 540px;
    background:
      radial-gradient(ellipse 260px 300px at 180px 200px, rgba(150,170,185,0.55), transparent 70%),
      linear-gradient(90deg, var(--veil-blue) 0%, #8fc6d8 30%, #e99a4a 52%, var(--skin-orange) 75%, #f4a43a 100%);
    -webkit-mask-image: linear-gradient(180deg, #000 0%, #000 55%, transparent 100%);
    mask-image: linear-gradient(180deg, #000 0%, #000 55%, transparent 100%);
  }

  .director-line {
    position: absolute;
    top: 40px; left: 0; width: 100%;
    text-align: center;
    font-family: "Cormorant Garamond", serif;
    font-weight: 500;
    font-size: 29px;
    color: var(--ink);
  }

  .title-block { position: absolute; left: 0; top: 0; }

  .studio-mark {
    position: absolute;
    left: 668px; top: 606px;
    display: flex; align-items: center; gap: 6px;
    font-family: "Questrial", sans-serif;
    font-size: 15px;
    letter-spacing: 1px;
    color: #1c7fb8;
  }
  .studio-mark .dot {
    width: 12px; height: 12px; border-radius: 50%;
    background: #1c7fb8;
  }

  .tagline {
    position: absolute;
    top: 862px; left: 249px;
    font-family: "Cormorant Garamond", serif;
    font-weight: 500;
    font-size: 31px;
    color: var(--tagline);
    letter-spacing: 0.5px;
  }

  .billing {
    position: absolute;
    left: 0; top: 1098px; width: 100%;
    text-align: center;
    font-family: "Questrial", sans-serif;
    color: var(--ink);
    text-transform: uppercase;
  }
  .billing p { line-height: 1; white-space: nowrap; }
  .billing .lead { font-size: 15.5px; letter-spacing: 0.6px; margin-bottom: 7px; }
  .billing .row { font-size: 14px; letter-spacing: 0.5px; margin-bottom: 6px; }
  .billing .row.small { font-size: 12.5px; }
  .billing .role { font-size: 9.5px; letter-spacing: 0.4px; }
</style>
</head>
<body>
  <main class="poster">
    <div class="key-art" role="img" aria-label="Two lovers touching foreheads, a woman in a sky-blue veil and a bearded man lit in warm orange"></div>

    <p class="director-line">A film by Adaeze N. Okonkwo</p>

    <svg class="title-block" width="810" height="860" viewBox="0 0 810 860" aria-label="Harbor of Glass">
      <text x="26" y="694" textLength="550" lengthAdjust="spacingAndGlyphs"
            font-family="Marcellus, serif" font-size="150" fill="#1f1a16">HARBOR</text>
      <text x="580" y="688" font-family="'Cormorant Garamond', serif" font-style="italic"
            font-size="64" fill="#1f1a16">of</text>
      <text x="304" y="836" textLength="480" lengthAdjust="spacingAndGlyphs"
            font-family="Marcellus, serif" font-size="150" fill="#1f1a16">GLASS</text>
    </svg>

    <div class="studio-mark"><span class="dot"></span>ORINDA FILMS</div>

    <p class="tagline">'A Matter of Family Honour'</p>

    <section class="billing">
      <p class="lead">Orinda Films <span class="role">presents</span> Harbor of Glass <span class="role">starring</span> Adaeze N. Okonkwo Rafael Quintero</p>
      <p class="row"><span class="role">Director of photography</span> Sam Lee <span class="role">editor</span> Henry Walsh <span class="role">production design</span> Martin Eklund</p>
      <p class="row"><span class="role">Music by</span> Amina Tounkara and Pierre Dumas de Valcourt</p>
      <p class="row small"><span class="role">Written produced and directed by</span> Adaeze N. Okonkwo</p>
    </section>
  </main>
</body>
</html>
```